Mechanical Engineering Business needs a Label Design for Bottle.

We need a Label design for 2 Bottle Sizes of Cutting Paste. This is used for Machine Work Shops big and small to do applications for different cutting processes. Example : Tapping / Broaching / Drilling / Reaming / Knurling / etc. An example of a similar product can be found at https://grivolex.com/product/16-oz-grivolex-bottle/ ... https://grivolex.com/product/2-oz-grivolex-bottle/ ... Our product will be named Mil - Gel or Milling - Gel with our Company logo attached. Currently, we are open to ideas and do not have any fixed concept.

```html
<!DOCTYPE html>
<html lang="en">
<head>
<meta charset="UTF-8">
<title>Milling-Gel Bottle Label</title>
<link href="https://fonts.googleapis.com/css2?family=Exo+2:wght@400;500;600;700&display=swap" rel="stylesheet">
<style>
  :root {
    --canvas: #ffffff;
    --label-dark: #1d1d1d;
    --label-dark-2: #2b2b2b;
    --logo-panel: #ecd896;
    --logo-ink: #7a1430;
    --silver-light: #f4f4f4;
    --silver-mid: #c9c9c9;
    --silver-dark: #8f8f8f;
    --title-ink: #1a1a1a;
    --text-light: #ffffff;
    --text-soft: #d6d6d6;
    --badge-fill: #bdbdbd;
    --tool-steel: #9c9c9c;
    --tool-steel-light: #d9d9d9;
  }
  * { margin: 0; padding: 0; box-sizing: border-box; }
  html, body {
    width: 1200px; height: 1200px; overflow: hidden;
    background: var(--canvas);
    font-family: "Exo 2", sans-serif;
  }
  .canvas { position: relative; width: 1200px; height: 1200px; }
  .label {
    position: absolute; left: 345px; top: 82px;
    width: 510px; height: 1037px;
  }
  .label-top {
    position: absolute; left: 0; top: 0; width: 510px; height: 657px;
    background: linear-gradient(180deg, var(--label-dark-2), var(--label-dark));
  }
  .logo-panel {
    position: absolute; left: 110px; top: 0; width: 300px; height: 255px;
    background: var(--logo-panel);
    display: flex; align-items: center; justify-content: center; gap: 14px;
  }
  .logo-mark {
    width: 34px; height: 34px; border-radius: 50%;
    background: var(--logo-ink);
  }
  .logo-name {
    font-weight: 600; font-size: 36px; color: var(--logo-ink);
    letter-spacing: 1px; text-transform: uppercase;
  }
  .tool-art {
    position: absolute; left: 87px; top: 277px; width: 330px; height: 330px;
    background: radial-gradient(circle at 50% 50%, var(--tool-steel-light), var(--tool-steel) 45%, var(--label-dark-2) 72%);
    border-radius: 50%;
  }
  .badge-ribbon { position: absolute; left: 30px; top: 370px; }
  .badge-round {
    position: absolute; left: 418px; top: 540px; width: 82px; height: 82px;
    border-radius: 50%; background: var(--badge-fill);
    border: 3px solid var(--text-light);
  }
  .formula {
    position: absolute; left: 0; top: 598px; width: 510px;
    text-align: center; color: var(--text-light);
    font-weight: 600; font-size: 30px; letter-spacing: 0.5px;
  }
  .title-band {
    position: absolute; left: 0; top: 657px; width: 510px; height: 120px;
    background: linear-gradient(180deg, var(--silver-dark) 0%, var(--silver-light) 10%, var(--silver-mid) 55%, var(--silver-light) 88%, var(--silver-dark) 100%);
    display: flex; align-items: center; justify-content: center;
  }
  .product-title {
    font-weight: 700; font-size: 68px; color: var(--title-ink); letter-spacing: 0.5px;
  }
  .label-bottom {
    position: absolute; left: 0; top: 777px; width: 510px; height: 260px;
    background: var(--label-dark);
    border-radius: 0 0 16px 16px;
  }
  .uses { position: absolute; left: 103px; top: 38px; color: var(--text-soft); }
  .uses-heading { color: var(--text-light); font-weight: 500; font-size: 19px; margin-bottom: 8px; }
  .uses-list { list-style: none; }
  .uses-list li { font-size: 23px; line-height: 30px; display: flex; align-items: center; gap: 6px; }
  .tick { width: 16px; height: 16px; }
  .facts { position: absolute; left: 330px; top: 34px; color: var(--text-light); font-weight: 600; }
  .facts p { font-size: 26px; line-height: 32px; }
  .facts .gap { margin-top: 20px; }
</style>
</head>
<body>
<main class="canvas">
  <section class="label">
    <div class="label-top">
      <div class="logo-panel">
        <span class="logo-mark"></span>
        <span class="logo-name">Corvant Tools</span>
      </div>
      <div class="tool-art" role="img" aria-label="Illustration of a cross-shaped tap and die wrench with a hex die"></div>
      <svg class="badge-ribbon" width="110" height="150" viewBox="0 0 110 150" aria-hidden="true">
        <polygon points="25,80 10,145 35,130 50,148 55,85" fill="var(--badge-fill)"/>
        <polygon points="85,80 100,145 75,130 60,148 55,85" fill="var(--badge-fill)"/>
        <circle cx="55" cy="60" r="48" fill="var(--badge-fill)" stroke="var(--text-light)" stroke-width="4"/>
      </svg>
      <div class="badge-round"></div>
      <p class="formula">THICK FORMULA</p>
    </div>
    <div class="title-band">
      <h1 class="product-title">Milling-Gel</h1>
    </div>
    <div class="label-bottom">
      <div class="uses">
        <p class="uses-heading">Exclusively for:</p>
        <ul class="uses-list">
          <li><svg class="tick" viewBox="0 0 16 16"><path d="M2 9l4 4 8-10" fill="none" stroke="#fff" stroke-width="2.5"/></svg>Tapping</li>
          <li><svg class="tick" viewBox="0 0 16 16"><path d="M2 9l4 4 8-10" fill="none" stroke="#fff" stroke-width="2.5"/></svg>Broaching</li>
          <li><svg class="tick" viewBox="0 0 16 16"><path d="M2 9l4 4 8-10" fill="none" stroke="#fff" stroke-width="2.5"/></svg>Drilling</li>
          <li><svg class="tick" viewBox="0 0 16 16"><path d="M2 9l4 4 8-10" fill="none" stroke="#fff" stroke-width="2.5"/></svg>Reaming</li>
          <li><svg class="tick" viewBox="0 0 16 16"><path d="M2 9l4 4 8-10" fill="none" stroke="#fff" stroke-width="2.5"/></svg>Knurling</li>
        </ul>
      </div>
      <div class="facts">
        <p>Increases:</p>
        <p>Tool Life Span</p>
        <p class="gap">Shake Well</p>
        <p class="gap">2 fl oz. (59 ml)</p>
      </div>
    </div>
  </section>
</main>
</body>
</html>
```